Pediatric Occupational Therapy Brochure Design

This design really needs to stand out, especially with all the wordage that I have included. These brochures will be given to doctors, future clients, and caregivers. I have included the logo on by brochure, so incorporating the same or similar colors would be fantastic. A trifold brochure would probably be best to fit all the information, as this is a new business and needs to convey all the information in a way that people will read.

Target Market(s)

Doctor's offices and caregivers of children with disabilities.

Industry/Entity Type

Health Care

Font styles to use
Serif
Sans Serif

Colors
33a6d7
85acd3
ffffff
33b8a4
86cfc7

Requirements
Must have
• I would like the same colors of the logo incorporated in the brochure design.
Nice to have
• I would like to see the butterfly somehow in the background or used in the design. Also a trifold or two page design would be greatly appreciated as long as the information can fit.

```html
<!DOCTYPE html>
<html lang="en">
<head>
<meta charset="utf-8">
<title>Pediatric Occupational Therapy Brochure – Inner Spread</title>
<link rel="stylesheet" href="https://fonts.googleapis.com/css2?family=Open+Sans:wght@400;600;700&display=swap">
<style>
  :root {
    --teal: #33b8a4;
    --teal-dark: #1f9d8c;
    --teal-light: #86cfc7;
    --sky: #33a6d7;
    --ink: #3a3a3a;
    --paper: #ffffff;
    --backdrop: #e4e4e4;
  }
  * { box-sizing: border-box; margin: 0; padding: 0; }
  html, body { width: 1200px; height: 1000px; overflow: hidden; }
  body {
    background: var(--backdrop);
    font-family: "Open Sans", Arial, sans-serif;
    color: var(--ink);
  }
  .spread {
    position: absolute; left: 40px; top: 67px;
    width: 1120px; height: 866px;
    display: flex; background: var(--paper);
    box-shadow: 0 6px 24px rgba(0,0,0,.18);
  }
  .panel {
    position: relative; width: 373.33px; height: 100%;
    border-right: 1px solid #ececec; overflow: hidden;
  }
  .panel:last-child { border-right: 0; }
  .pill {
    display: inline-block; background: var(--teal); color: #fff;
    font-weight: 600; font-size: 15px; padding: 4px 16px;
    border-radius: 14px; letter-spacing: .2px;
  }
  .subhead {
    color: var(--teal); font-weight: 700; font-size: 13px;
    text-decoration: underline; margin: 12px 0 6px;
  }
  .subhead.first { margin-top: 0; }
  .body-text { font-size: 12.5px; line-height: 1.45; text-align: justify; }
  .block { position: absolute; left: 30px; right: 30px; }
  .checklist { list-style: none; font-size: 12.5px; line-height: 1.4; }
  .checklist li { position: relative; padding-left: 16px; margin-bottom: 2px; }
  .checklist li::before {
    content: ""; position: absolute; left: 2px; top: 4px;
    width: 4px; height: 8px; border: solid var(--teal);
    border-width: 0 2px 2px 0; transform: rotate(45deg);
  }
  .photo { position: absolute; left: 0; right: 0; bottom: 246px; }
  .photo-child { top: 360px; background: linear-gradient(135deg, #9bb88a, #d9c2b8 55%, #6fa860); }
  .photo-hands { top: 385px; background: linear-gradient(135deg, #c9b8a0, #efe6da 50%, #c85b4a); }
  .photo-play { top: 410px; background: linear-gradient(135deg, #c7ccd4, #8d96a6 50%, #4f9c4a); }
  .wave-band { position: absolute; left: 0; top: 520px; width: 1120px; height: 100px; z-index: 2; }
</style>
</head>
<body>
<main class="spread">

  <section class="panel about">
    <div class="block" style="top:40px">
      <span class="pill">ABOUT US</span>
      <p class="body-text" style="margin-top:14px">My name is Elena and I am a pediatric Occupational Therapist. I was born and raised in the Rio Grande Valley and have provided services to the pediatric and adult population since 2012. I am currently certified in Neuro-Developmental Treatment of Children with Cerebral Palsy and Other Neuromotor Disorders and have had the pleasure of working with children with various disorders and disabilities. I am a dedicated OTR that works with each client and family to develop a specific plan of care to maximize functional ability across all environments.</p>
    </div>
    <div class="photo photo-child" role="img" aria-label="Photo of a young girl smiling and looking up during therapy"></div>
    <div class="block" style="top:645px">
      <p class="subhead first">Role of Occupational Therapy with Children</p>
      <p class="body-text">Occupational therapists work with children, who have challenges, to fully participate in normal daily activities. Those challenges may be due to developmental delay, ADD/ADHD, autism, chromosomal differences, injury, trauma, and many others. An occupational therapist evaluates to assess areas of difficulty as well as strengths, and treat the child based on his or her specific needs.</p>
    </div>
  </section>

  <section class="panel services">
    <div class="block" style="top:40px">
      <span class="pill">Occupational Therapy Services</span>
      <p class="subhead">Occupational Therapy Goals</p>
      <p class="body-text">A child’s occupation is to be a kid! Through the use of play, I can help children acquire the skills needed for the job of living. These include, but are not limited to:</p>
      <ul class="checklist" style="margin-top:8px">
        <li>Promoting independence in daily living skills-including dress, grooming, and feeding</li>
        <li>Facilitating developmental play skills</li>
        <li>Improving fine motor and eye-hand coordination skills</li>
        <li>Improving sensory processing skills such as organization, self-regulation and behavioral state</li>
      </ul>
    </div>
    <div class="photo photo-hands" role="img" aria-label="Photo of a therapist's hands guiding a child during a play activity"></div>
    <div class="block" style="top:630px">
      <ul class="checklist">
        <li>Improving visual motor/visual perceptual skills including writing and coloring</li>
        <li>Addressing orthopedic complications and helping to increase function through the use of splinting and taping</li>
        <li>Improving balance and coordination skills through play</li>
      </ul>
    </div>
  </section>

  <section class="panel benefits">
    <div class="block" style="top:40px">
      <span class="pill">Benefit from Occupational Therapy</span>
      <ul class="checklist" style="margin-top:12px">
        <li>ADD/ADHD</li>
        <li>Auditory Processing Disorders</li>
        <li>Autism Spectrum Disorders</li>
        <li>Cancer/Leukemia</li>
        <li>Cerebral Palsy/Congenital Heart Disease</li>
        <li>Developmental Delay</li>
        <li>Genetic Disorders/Birth Defects</li>
        <li>Orthopedic Injuries or Surgery</li>
        <li>Sensory Integration Disorders</li>
        <li>Trauma Brain Injuries</li>
        <li>Tracheostomy and/or ventilator dependency</li>
        <li>And any condition that affects a child’s growth and development</li>
      </ul>
    </div>
    <div class="photo photo-play" role="img" aria-label="Photo of a therapist supporting a child on an exercise ball among colourful cones"></div>
    <div class="block" style="top:615px">
      <p class="subhead first">Parental Involvement:</p>
      <p class="body-text">Each child’s success is strongly dependent upon the caregiver’s involvement. Therapy does not stop when the session ends and must be carried over across all environments in a child’s life. I specialize in working with parents and caregivers to ensure home programs are in place to make each child’s progress the best.</p>
    </div>
  </section>

  <svg class="wave-band" viewBox="0 0 1120 100" preserveAspectRatio="none" aria-hidden="true">
    <path d="M0 60 C300 34 700 22 1120 0 L1120 40 C700 60 300 82 0 100 Z" fill="var(--teal-dark)"/>
    <path d="M0 100 C300 82 700 60 1120 40 L1120 100 Z" fill="var(--paper)"/>
  </svg>

</main>
</body>
</html>
```